I am looking for a flyer design for my upcoming symposium. Here are the details for the flyer and pictures of speakers are attached.

Name of Symposium: Layered and Dynamic Cellmap Colloquium, Sponsored by the Harlow Chromatin Institute and the Department of Bioengineering
Date: January 8, 2018
Location: Whitacre Auditorium, Denholm Center for Applied Discovery, 2716 Meadowgate Ave, Philadelphia, PA 19131

Reception to follow after the symposium.

Also, please add - Register and upload abstracts for the symposium at www.colloquiumsignup-example.org. Registration and abstract submission closes on January 4, 2018.

Keynote Speaker:
Marta Linsky, Ph.D.
NVRA Director General; Professor, Lyceum of Avrenne; Director, Genetics and Developmental Biology at Institut Valmorel
Lyceum of Avrenne, NVRA, Institut Valmorel
"Title of talk TBA."

Speakers:
Rhea Dunsworth, Ph.D.
Assistant Professor of Cell and Developmental Biology
Aldergrove University, AUMC
"Title of talk TBA."

Owen Brakely, Ph.D.
Assistant Professor of Genetics
"Title of talk TBA."

Lia Varnet, Ph.D.
Professor, Kestrel University
Otto Feldmark Center for Molecular Medicine
"Title of talk TBA."

Jun Mao, Ph.D.
Professor of Cellular and Molecular Medicine
Western Coastal Institute of Science
"Title of talk TBA."

Lin Zhou, Ph.D.
Associate Professor of Pediatrics
The Riverside Youth Hospital of Philadelphia
"Spatial genome re-organization between fetal and adult hematopoietic stem cells."

Mei Lao, Ph.D.
Professor, Department of Genetics
Ellsworth Medical School
"Title of talk TBA."

```html
<!DOCTYPE html>
<html lang="en">
<head>
<meta charset="utf-8">
<title>Layered and Dynamic Cellmap Colloquium</title>
<link rel="stylesheet" href="https://fonts.googleapis.com/css2?family=Arimo&family=PT+Sans:wght@400;700&display=swap">
<style>
:root{
  --blue:#4d97c9;
  --blue-text:#3d8ec6;
  --ink:#2b2b2b;
  --grey-text:#555759;
  --info-grey:#8c8c8c;
  --panel:#e3e4e5;
  --dark:#333436;
  --header-dark:#34414f;
  --white:#ffffff;
}
*{margin:0;padding:0;box-sizing:border-box}
html,body{width:1002px;height:1200px;overflow:hidden;background:#fff}
.flyer{position:relative;width:1002px;height:1200px;overflow:hidden;font-family:"PT Sans",sans-serif;color:var(--ink)}
.header-art{position:absolute;left:0;top:0}
.title{position:absolute;left:38px;top:120px;color:var(--white);font-family:"Arimo",sans-serif;font-weight:400;font-size:49px;line-height:57px;letter-spacing:.2px}
.sponsor{position:absolute;left:38px;top:360px;font-size:21px;line-height:28px;color:var(--grey-text)}
.partners{position:absolute;left:38px;top:470px;display:flex;align-items:center;gap:34px}
.partner{display:flex;align-items:center;gap:10px;font-size:20px;color:var(--blue-text);font-weight:700}
.partner .mark{width:22px;height:22px;background:var(--blue-text)}
.partner .mark.round{border-radius:50%}
.info-box{position:absolute;left:582px;top:251px;width:387px;height:300px;background:var(--info-grey);color:var(--white);text-align:center;box-shadow:0 14px 14px -8px rgba(0,0,0,.3)}
.info-box .date{font-size:27px;padding-top:44px;height:106px}
.info-box hr{border:0;border-top:1.5px solid rgba(255,255,255,.85);width:310px;margin:0 auto}
.info-box .venue,.info-box .address{font-size:19px;line-height:30px;padding:18px 0 16px}
.speakers{position:absolute;left:28px;top:580px;width:941px;height:520px;background:var(--panel)}
.speaker{position:absolute;width:250px;text-align:center;font-size:11.5px;line-height:15.5px;color:var(--ink);font-family:"Arimo",sans-serif}
.speaker .photo{display:block;width:122px;height:120px;margin:0 auto 10px;border:3px solid var(--white);box-shadow:0 3px 4px rgba(0,0,0,.25)}
.speaker .name{color:var(--blue-text)}
.speaker.keynote .role{font-family:"PT Sans",sans-serif;font-size:17px;line-height:22px;margin-top:6px}
.speaker.keynote .name{font-family:"PT Sans",sans-serif;font-size:15px;line-height:20px;margin-bottom:2px}
.speaker.keynote .detail{font-size:12px;line-height:16px}
.footer-art{position:absolute;left:0;top:1032px}
.deadline{position:absolute;left:38px;top:1082px;color:var(--white);font-size:18.5px;line-height:30px}
.register{position:absolute;left:380px;top:1120px;width:610px;color:var(--white);font-size:16px;text-align:center}
</style>
</head>
<body>
<div class="flyer">
  <svg class="header-art" width="1002" height="330" viewBox="0 0 1002 330">
    <defs>
      <linearGradient id="helixTone" x1="0" y1="0" x2="1" y2="0">
        <stop offset="0" stop-color="#3b4a59"/>
        <stop offset=".55" stop-color="#2e3b48"/>
        <stop offset="1" stop-color="#435363"/>
      </linearGradient>
    </defs>
    <polygon points="0,0 1002,0 1002,142 0,57" fill="url(#helixTone)" role="img" aria-label="Dark photograph of a DNA double helix"/>
    <polygon points="0,57 1002,142 1002,245 0,325" fill="var(--blue)"/>
  </svg>
  <h1 class="title">Layered and Dynamic<br>Cellmap Colloquium</h1>

  <p class="sponsor">Sponsored by the Harlow Chromatin Institute<br>and the Department of Bioengineering</p>
  <div class="partners">
    <div class="partner"><span class="mark round"></span>Harlow Chromatin Institute</div>
    <div class="partner"><span class="mark"></span>Kellerton Engineering</div>
  </div>

  <div class="info-box">
    <p class="date">January 8, 2018</p>
    <hr>
    <p class="venue">Whitacre Auditorium, Denholm<br>Center for Applied Discovery</p>
    <hr>
    <p class="address">2716 Meadowgate Ave,<br>Philadelphia, PA 19131</p>
  </div>

  <section class="speakers">
    <div class="speaker keynote" style="left:-10px;top:33px">
      <span class="photo" role="img" aria-label="Portrait of Marta Linsky" style="background:linear-gradient(160deg,#6b4a3a,#c9a58e 60%,#e6dcd5)"></span>
      <p class="role">Keynote Speaker</p>
      <p class="name">Marta Linsky, Ph.D.</p>
      <p class="detail">NVRA Director General;<br>Professor, Lyceum of Avrenne;<br>Director, Genetics and<br>Developmental Biology at<br>Institut Valmorel Lyceum of Avrenne,<br>NVRA, Institut Valmorel<br>"Title of talk TBA."</p>
    </div>
    <div class="speaker" style="left:214px;top:33px">
      <span class="photo" role="img" aria-label="Portrait of Rhea Dunsworth" style="background:linear-gradient(160deg,#c98a4a,#8a5a3c 55%,#d94a3f)"></span>
      <p class="name">Rhea Dunsworth, Ph.D.</p>
      <p>Assistant Professor of Cell and<br>Developmental Biology<br>Aldergrove University, AUMC<br>"Title of talk TBA."</p>
    </div>
    <div class="speaker" style="left:456px;top:33px">
      <span class="photo" role="img" aria-label="Portrait of Owen Brakely" style="background:linear-gradient(160deg,#8c3b2e,#c98f74 55%,#e8e4e0)"></span>
      <p class="name">Owen Brakely, Ph.D.</p>
      <p>Assistant Professor of Genetics<br>Aldergrove University, AUMC<br>"Title of talk TBA."</p>
    </div>
    <div class="speaker" style="left:696px;top:33px">
      <span class="photo" role="img" aria-label="Portrait of Lia Varnet" style="background:linear-gradient(160deg,#6f7266,#3a2e28 50%,#c6a592)"></span>
      <p class="name">Lia Varnet, Ph.D.</p>
      <p>Professor, Kestrel University<br>Otto Feldmark Center for Molecular<br>Medicine<br>"Title of talk TBA."</p>
    </div>
    <div class="speaker" style="left:214px;top:269px">
      <span class="photo" role="img" aria-label="Portrait of Jun Mao" style="background:linear-gradient(160deg,#e9e7e4,#c99a7a 55%,#2c2c2e)"></span>
      <p class="name">Jun Mao, Ph.D.</p>
      <p>Professor of Cellular and Molecular<br>Medicine<br>Western Coastal Institute of Science<br>"Title of talk TBA."</p>
    </div>
    <div class="speaker" style="left:441px;top:269px;width:280px">
      <span class="photo" role="img" aria-label="Portrait of Lin Zhou" style="background:linear-gradient(160deg,#8a6a55,#caa083 45%,#8fb6dc)"></span>
      <p class="name">Lin Zhou, Ph.D.</p>
      <p>Associate Professor of Pediatrics<br>The Riverside Youth Hospital of Philadelphia<br>"Spatial genome re-organization<br>between fetal and adult hematopoietic stem cells."</p>
    </div>
    <div class="speaker" style="left:696px;top:269px">
      <span class="photo" role="img" aria-label="Portrait of Mei Lao" style="background:linear-gradient(160deg,#4f6a3c,#2f2a26 45%,#d7b8a2)"></span>
      <p class="name">Mei Lao, Ph.D.</p>
      <p>Professor, Department of Genetics<br>Ellsworth Medical School<br>"Title of talk TBA."</p>
    </div>
  </section>

  <svg class="footer-art" width="1002" height="168" viewBox="0 0 1002 168">
    <polygon points="0,15 28,0 28,15" fill="var(--blue)"/>
    <polygon points="312,59 1002,59 1002,146 365,146" fill="var(--dark)"/>
    <polygon points="0,15 285,15 365,146 0,146" fill="var(--blue)"/>
    <rect x="0" y="146" width="1002" height="22" fill="var(--blue)"/>
  </svg>
  <p class="deadline">Registration and abstract<br>submission closes on<br>January 4, 2018.</p>
  <p class="register">Register and upload abstracts for the symposium at www.colloquiumsignup-example.org</p>
</div>
</body>
</html>
```